Modern and strong website design for a Dutch crowdsourcing company
.

We are startup company providing crowdsourcing of administrative and customers service tasks for larger companies and other organizations. We offer cost savings and scale-ability combined with higher quality of execution. We will soon enter the market and need a website that has two major target groups: 1. Our corporate customers 2. The mainly younger crowd executing the tasks on our platform.
The target group of customers are Influencers and decision makers with companies and other organizations in with large administrative and customer service departments. Most information in the startup phase will be targeting this group.
The target group of future crowd workers will be heterogeneous, from students to stay at home mums or night shift workers who want to earn some extra money by performing easy to execute microtasks in the cloud. We will target both Dutch and international workers.

The website must be developed for browsing on a computer but also be optimized for mobile devices and tablets.
The website must be optimized and tested for the major browsers on windows, macOS and mobile devices.

For the minimum requirement for the website see attached wireframes

The present landing page http://thepinegladeloft.com and logo are not reflecting our preferences!
See enclosed a new logo that stands for both the crowdwork (performed for our customers) and the crowd (the pine glade loft).

Target Market(s)

see tekst above.

Industry/Entity Type

Business Service

Coding

Coded - Design and coding required

Number of Pages Required

5+ page

Font styles to use
Sans Serif
Other font styles liked:
• Lato, Open Sans

Colors

Designer to choose colors to be used in the design.

Requirements
Must have
• start devider screen
• home page displaying business and worker information
• a page displaying only info for businesses
• a page displaying only info for workers
• a contact form
• a reviews page
• color scheme from logo
• responsiveness!
Nice to have
• Nice animations
• overlapping blocks, animated on scroll
• lightbox effects if applicable
• animated mobile menu icon and menu itself

```html
<!DOCTYPE html>
<html lang="en">
<head>
<meta charset="utf-8">
<title>The Pine Glade Loft</title>
<link rel="stylesheet" href="https://fonts.googleapis.com/css2?family=Open+Sans:ital,wght@0,400;0,600;0,700;0,800;1,700&display=swap">
<style>
:root{
  --orange:#f39322;
  --orange-dark:#e07c10;
  --navy:#0c1c33;
  --ink:#333a44;
  --grey:#6d7480;
  --card:#ececec;
  --white:#ffffff;
}
*{box-sizing:border-box;margin:0;padding:0}
html,body{width:1200px;height:3260px;overflow:hidden}
body{font-family:"Open Sans",Arial,sans-serif;color:var(--ink);background:var(--white);position:relative}
.brand{display:flex;align-items:center;gap:10px;color:var(--orange);font-weight:800;font-size:24px;line-height:1;text-decoration:none}
.brand-dot{width:16px;height:16px;border-radius:50%;background:var(--orange)}
.btn{display:inline-block;font-size:13px;font-weight:700;letter-spacing:.5px;text-transform:uppercase;padding:12px 26px;border-radius:3px;text-decoration:none}
.btn-orange{background:var(--orange);color:var(--white)}
.btn-light{background:var(--white);color:var(--orange)}

.site-header{position:absolute;top:0;left:0;width:1200px;height:120px;display:flex;align-items:center;padding:0 56px 0 40px}
.main-nav{display:flex;gap:34px;margin-left:70px}
.main-nav a{font-size:13px;font-weight:700;color:var(--ink);text-decoration:none;text-transform:uppercase}
.main-nav a.active{color:var(--orange)}
.site-header .btn{margin-left:auto}

.hero{position:absolute;top:120px;left:0;width:1200px;height:600px;background:radial-gradient(circle at 72% 25%,#5c9bd4 0%,#1f4f88 30%,#0f2c52 60%,#081a33 100%)}
.hero-box{position:absolute;left:108px;top:218px;width:580px;padding:30px 28px;background:rgba(5,18,38,.78);border:1px solid rgba(255,255,255,.25)}
.hero-box h1{color:var(--white);font-size:29px;line-height:1.3;font-weight:700;margin-bottom:26px}
.hero-box .btn{margin-right:14px}

.benefits{position:absolute;top:720px;left:0;width:1200px;height:260px;background:linear-gradient(#1a1d22,#0d0f12);display:flex;justify-content:center;gap:40px;padding-top:84px}
.benefit{display:flex;gap:18px;width:320px}
.benefit-icon{flex:0 0 88px;height:88px;border-radius:8px;background:#f4efe6;display:flex;align-items:center;justify-content:center}
.benefit h3{color:var(--orange);font-size:16px;font-weight:700;margin-bottom:4px;line-height:1.3}
.benefit p{color:#e4e4e4;font-size:13px;line-height:1.45}

.section-title{display:flex;align-items:center;gap:14px;font-size:20px;font-weight:800;text-transform:uppercase;letter-spacing:.5px}
.lead{font-size:14px;line-height:1.75;margin-top:22px}

.business{position:absolute;top:1040px;left:0;width:1200px;height:400px}
.business .photo{position:absolute;left:72px;top:20px;width:470px;height:340px;background:linear-gradient(160deg,#dfe8f2,#9fb4cb 55%,#5a6f88)}
.business .copy{position:absolute;left:574px;top:28px;width:560px;color:var(--grey)}
.business .section-title{color:var(--ink)}
.business .btn{margin-top:26px}

.workers{position:absolute;top:1480px;left:0;width:1200px;height:500px;background:linear-gradient(90deg,var(--orange-dark),var(--orange))}
.workers .copy{position:absolute;left:72px;top:70px;width:560px;color:var(--white)}
.workers .btn{margin-top:26px}
.workers .photo{position:absolute;left:664px;top:72px;width:466px;height:350px;background:linear-gradient(150deg,#c9b9a2,#8a7b6b 50%,#4c4540)}

.reviews{position:absolute;top:2040px;left:0;width:1200px;height:420px}
.reviews .section-title{justify-content:center;color:var(--ink);margin-top:20px}
.review-list{display:flex;gap:28px;justify-content:center;margin-top:44px}
.review{width:330px}
.review-card{position:relative;height:160px;background:var(--card);border-radius:4px;padding:18px 20px 18px 52px;font-size:12px;line-height:1.6;color:var(--grey)}
.review-card::before{content:"\201C";position:absolute;left:16px;top:0;font-size:60px;font-weight:800;color:var(--ink);line-height:1}
.review-card::after{content:"\201D";position:absolute;right:96px;bottom:-14px;font-size:60px;font-weight:800;color:var(--ink);line-height:1}
.avatar{position:absolute;right:18px;bottom:-40px;width:80px;height:80px;border-radius:50%;background:linear-gradient(#d9c3ad,#8f7764);border:4px solid var(--white);box-shadow:0 0 0 2px var(--orange)}
.review-name{font-style:italic;font-weight:700;font-size:15px;color:var(--ink);margin:18px 0 0 8px}
.dots{display:flex;gap:8px;justify-content:center;margin-top:26px}
.dots span{width:10px;height:10px;border-radius:50%;background:#ccc}
.dots span.on{background:var(--orange)}

.contact{position:absolute;top:2480px;left:0;width:1200px;height:560px;background:linear-gradient(120deg,rgba(243,147,34,.92),rgba(226,128,20,.9)),linear-gradient(90deg,#b77a3c,#e5a764,#a36a34)}
.contact .section-title{justify-content:center;color:var(--white);margin-top:56px}
.contact-form{position:absolute;left:112px;top:150px;width:976px}
.field-row{display:flex;gap:24px}
.field{flex:1;height:48px;background:rgba(255,255,255,.28);border:1px solid rgba(255,255,255,.55);color:var(--white);font-size:13px;padding:14px 16px}
.field-area{height:140px;margin-top:22px}
.contact-form .btn{display:block;width:200px;margin:40px auto 0;text-align:center}

.site-footer{position:absolute;top:3040px;left:0;width:1200px;height:180px;text-align:center}
.site-footer .brand{justify-content:center;margin-top:44px;font-size:30px}
.foot-nav{display:flex;justify-content:center;gap:38px;margin-top:40px}
.foot-nav a{font-size:12px;font-weight:700;color:var(--ink);text-decoration:none}
.foot-nav a.active{color:var(--orange)}
.bottom-bar{position:absolute;top:3220px;left:0;width:1200px;height:40px;background:var(--navy);color:#c8cdd6;font-size:11px;display:flex;align-items:center;padding:0 24px;gap:28px}
.bottom-bar span{display:flex;align-items:center;gap:7px}
.bottom-bar .copy-note{margin-left:auto}
</style>
</head>
<body>

<header class="site-header">
  <a class="brand" href="#"><span class="brand-dot"></span>The Pine Glade Loft</a>
  <nav class="main-nav">
    <a class="active" href="#">Home</a>
    <a href="#">For businesses</a>
    <a href="#">For workers</a>
  </nav>
  <a class="btn btn-orange" href="#">Contact us</a>
</header>

<section class="hero" role="img" aria-label="Photo of a glowing globe above a network of business people silhouettes on a blue background">
  <div class="hero-box">
    <h1>We provide crowdsourcing of administrative and customers service tasks for larger companies and other organizations.</h1>
    <a class="btn btn-orange" href="#">For businesses</a>
    <a class="btn btn-light" href="#">For workers</a>
  </div>
</section>

<section class="benefits">
  <div class="benefit">
    <div class="benefit-icon">
      <svg width="50" height="50" viewBox="0 0 50 50" fill="none" stroke="#f39322" stroke-width="3"><circle cx="18" cy="25" r="12"/><circle cx="34" cy="25" r="12"/><path d="M18 19v12M34 19v12"/></svg>
    </div>
    <div><h3>Cost Savings</h3><p>We offer cost savings by crowdsourcing your projects</p></div>
  </div>
  <div class="benefit">
    <div class="benefit-icon">
      <svg width="54" height="54" viewBox="0 0 54 54" fill="none" stroke="#f39322" stroke-width="3"><circle cx="27" cy="27" r="6"/><circle cx="9" cy="9" r="4"/><circle cx="45" cy="9" r="4"/><circle cx="9" cy="45" r="4"/><circle cx="45" cy="45" r="4"/><path d="M12 12l10 10M42 12L32 22M12 42l10-10M42 42L32 32"/></svg>
    </div>
    <div><h3>Scale-ability Combined</h3><p>Scale-ability combined for all administrative and customers service tasks</p></div>
  </div>
  <div class="benefit">
    <div class="benefit-icon">
      <svg width="50" height="50" viewBox="0 0 50 50" fill="none" stroke="#f39322" stroke-width="3"><rect x="8" y="6" width="28" height="36" rx="2"/><path d="M14 16h16M14 24h16M14 32h8"/><circle cx="37" cy="35" r="9" fill="#f4efe6"/><path d="M33 35l3 3 5-6"/></svg>
    </div>
    <div><h3>Higher Quality of Execution</h3><p>The Pine Glade Loft offers higher quality of execution for all projects on the platform.</p></div>
  </div>
</section>

<section class="business">
  <div class="photo" role="img" aria-label="Photo looking up at office towers against a cloudy sky"></div>
  <div class="copy">
    <h2 class="section-title">
      <svg width="30" height="30" viewBox="0 0 30 30" fill="#333a44"><rect x="4" y="4" width="10" height="24"/><rect x="16" y="10" width="10" height="18"/></svg>
      For businesses
    </h2>
    <p class="lead">Lorem ipsum dolor sit amet, consectetuer adipiscing elit, sed diam nonummy nibh euismod tincidunt ut laoreet dolore magna aliquam erat volutpat. Ut wisi enim ad minim veniam, quis nostrud exerci tation ullamcorper suscipit lobortis nisl ut aliquip ex ea commodo consequat.</p>
    <p class="lead">Duis autem vel eum iriure dolor in hendrerit in vulputate velit esse molestie consequat, vel illum dolore eu feugiat nulla facilisis at vero eros et accumsan et iusto odio dignissim qui blandit praesent luptatum zzril delenit augue duis dolore te feugait nulla facilisi.</p>
    <a class="btn btn-orange" href="#">Get started now</a>
  </div>
</section>

<section class="workers">
  <div class="copy">
    <h2 class="section-title">
      <svg width="34" height="28" viewBox="0 0 34 28" fill="#ffffff"><circle cx="17" cy="8" r="6"/><path d="M6 28c0-7 5-11 11-11s11 4 11 11z"/><circle cx="5" cy="11" r="4"/><circle cx="29" cy="11" r="4"/></svg>
      For workers
    </h2>
    <p class="lead">Lorem ipsum dolor sit amet, consectetuer adipiscing elit, sed diam nonummy nibh euismod tincidunt ut laoreet dolore magna aliquam erat volutpat. Ut wisi enim ad minim veniam, quis nostrud exerci tation ullamcorper suscipit lobortis nisl ut aliquip ex ea commodo consequat.</p>
    <p class="lead">Duis autem vel eum iriure dolor in hendrerit in vulputate velit esse molestie consequat, vel illum dolore eu feugiat nulla facilisis at vero eros et accumsan et iusto odio dignissim qui blandit praesent luptatum zzril delenit augue duis dolore te feugait nulla facilisi.</p>
    <a class="btn btn-light" href="#">Get started now</a>
  </div>
  <div class="photo" role="img" aria-label="Overhead photo of young people working on laptops around a table"></div>
</section>

<section class="reviews">
  <h2 class="section-title">
    <svg width="32" height="28" viewBox="0 0 32 28" fill="#333a44"><path d="M2 2h20v14H10l-6 5v-5H2z"/><path d="M24 8h6v14h-2v5l-6-5h-10v-4h12z"/></svg>
    Reviews
  </h2>
  <div class="review-list">
    <div class="review">
      <div class="review-card">Lorem ipsum dolor sit amet, consectetuer adipiscing elit, sed diam nonummy nibh euismod tincidunt ut laoreet dolore magna aliquam erat volutpat. Ut wisi enim ad minim veniam.<span class="avatar" role="img" aria-label="Portrait of reviewer"></span></div>
      <p class="review-name">Marieke Jansen</p>
    </div>
    <div class="review">
      <div class="review-card">Lorem ipsum dolor sit amet, consectetuer adipiscing elit, sed diam nonummy nibh euismod tincidunt ut laoreet dolore magna aliquam erat volutpat. Ut wisi enim ad minim veniam.<span class="avatar" role="img" aria-label="Portrait of reviewer"></span></div>
      <p class="review-name">Lotte de Vries</p>
    </div>
    <div class="review">
      <div class="review-card">Lorem ipsum dolor sit amet, consectetuer adipiscing elit, sed diam nonummy nibh euismod tincidunt ut laoreet dolore magna aliquam erat volutpat. Ut wisi enim ad minim veniam.<span class="avatar" role="img" aria-label="Portrait of reviewer"></span></div>
      <p class="review-name">Daan Visser</p>
    </div>
  </div>
  <div class="dots"><span class="on"></span><span></span><span></span></div>
</section>

<section class="contact" role="img" aria-label="Photo of a team at work, tinted orange, behind the contact form">
  <h2 class="section-title">
    <svg width="28" height="32" viewBox="0 0 28 32" fill="#ffffff"><path d="M10 2c2 0 3 1 3 3v11l2-1c2-1 4 0 4 2l3-1c2 0 3 1 3 3v5c0 5-4 8-9 8h-2c-4 0-6-2-8-5L2 21c-1-2 1-4 3-3l2 2V5c0-2 1-3 3-3z"/></svg>
    Contact us
  </h2>
  <form class="contact-form">
    <div class="field-row">
      <div class="field">Your Name</div>
      <div class="field">Your Email</div>
      <div class="field">Your Subject</div>
    </div>
    <div class="field field-area">Message</div>
    <a class="btn btn-light" href="#">Send message</a>
  </form>
</section>

<footer class="site-footer">
  <a class="brand" href="#"><span class="brand-dot"></span>The Pine Glade Loft</a>
  <nav class="foot-nav">
    <a class="active" href="#">HOME</a>
    <a href="#">FOR BUSINESSES</a>
    <a href="#">FOR WORKERS</a>
  </nav>
</footer>

<div class="bottom-bar">
  <span><svg width="12" height="12" viewBox="0 0 12 12" fill="#f39322"><path d="M2 1l2 0 1 3-1.5 1a7 7 0 0 0 3.5 3.5L8 7l3 1v2c0 1-1 1-1 1C5 11 1 7 1 2c0 0 0-1 1-1z"/></svg>+31 20 555 0192</span>
  <span><svg width="13" height="10" viewBox="0 0 13 10" fill="none" stroke="#f39322" stroke-width="1.5"><rect x="1" y="1" width="11" height="8"/><path d="M1 1l5.5 4L12 1"/></svg>info@thepinegladeloft.com</span>
  <span class="copy-note">Copyright © 2017 The Pine Glade Loft</span>
</div>

</body>
</html>
```